Plakat-Design für Kosmetikinstitut
Zielgruppe
edles Kosmetikinstitut der gehobenen Kategorie
Zielgruppe Frauen und Männer die wert auf Qualität legen
Aufgabenstellung
Das Poster soll fürs Schaufenster, sowie Messestand, sowie Gehwegreiter sein. Es soll vermitteln was wir anbieten. Beim Dateiupload stelle ich weitere Infos über das Studio zusammen.
Bilder und Logo im Anhang. Logo ist in verschiedenen Farben erhältlich. Bilder müssen nicht verwendet werden, dienen nur der Orientierung.
Slogan vom Institut ist ... einfach schön
anbei sende ich och unseren Flyer
Es sollten die Kontaktdaten wie Adresse, Homepage und Telefonnummer be isein

```html
<!DOCTYPE html>
<html lang="de">
<head>
<meta charset="utf-8">
<title>Kosmetikinstitut Velourna – Plakat</title>
<link rel="stylesheet" href="https://fonts.googleapis.com/css2?family=Open+Sans:wght@300;400&family=Raleway:wght@200;300&display=swap">
<style>
  :root {
    --paper: #ffffff;
    --band: #c3c3c3;
    --taupe: #978473;
    --taupe-deep: #7e7062;
    --slate: #8a8a8a;
    --ink: #222222;
    --brand: #9a8878;
    --white: #ffffff;
  }
  html, body { margin: 0; padding: 0; overflow: hidden; background: var(--paper); }
  .poster {
    position: relative; width: 847px; height: 1200px; overflow: hidden;
    background: var(--paper); font-family: "Open Sans", sans-serif; font-weight: 300;
  }
  .abs { position: absolute; }
  .band { left: 0; top: 442px; width: 847px; height: 31px; background: var(--band); }
  .hero-photo {
    left: 0; top: 0; width: 440px; height: 473px;
    background: radial-gradient(ellipse at 45% 40%, #f3dccf 0%, #e8c8b5 45%, #f4eeea 80%, rgba(255,255,255,0) 100%);
  }
  .brand { left: 300px; top: 160px; width: 366px; text-align: center; color: var(--brand); font-family: "Raleway", sans-serif; font-weight: 300; }
  .brand-kind { font-size: 16px; letter-spacing: 8.4px; line-height: 20px; }
  .brand-name { font-size: 37px; letter-spacing: 21px; line-height: 46px; margin-right: -21px; }
  .brand-tagline { font-size: 11px; letter-spacing: 1.6px; margin-top: 4px; }

  .col-taupe { left: 0; top: 473px; width: 389px; height: 727px; background: var(--taupe); }
  .col-slate { left: 389px; top: 473px; width: 458px; height: 727px; background: var(--slate); }
  .services-panel { left: 106px; top: 522px; width: 327px; height: 678px; background: var(--taupe-deep); }
  .services-title { left: 107px; top: 496px; font-size: 18px; color: var(--ink); line-height: 24px; }

  .svc-head, .svc-item { left: 175px; color: var(--white); white-space: nowrap; }
  .svc-head { width: 258px; font-size: 18px; line-height: 22px; }
  .svc-head.ruled { border-bottom: 1px solid rgba(255,255,255,0.8); }
  .svc-item { font-size: 13.5px; line-height: 20px; }

  .slogan {
    left: 480px; top: 845px; transform: translate(-50%, -50%) rotate(-90deg);
    white-space: nowrap; color: var(--white); font-family: "Raleway", sans-serif;
    font-weight: 200; font-size: 52px; letter-spacing: 13px; line-height: 60px;
  }

  .photo-facial { left: 510px; top: 483px; width: 337px; height: 236px;
    background: linear-gradient(135deg, #f2e4e0 0%, #eccfc8 50%, #d9b3a8 100%); }
  .photo-brushes { left: 510px; top: 724px; width: 337px; height: 230px;
    background: linear-gradient(160deg, #efe9e6 0%, #c9b3a6 45%, #6b5148 100%); }

  .info-box { left: 510px; top: 957px; width: 337px; height: 69px; background: var(--taupe-deep); }
  .info-text { left: 527px; top: 969px; color: var(--white); font-size: 18px; line-height: 22px; }

  .contact { left: 574px; top: 1035px; color: var(--ink); font-size: 19px; line-height: 21.8px; font-weight: 300; }
  .contact p { margin: 0; }
</style>
</head>
<body>
<main class="poster">
  <div class="abs band"></div>
  <div class="abs hero-photo" role="img" aria-label="Porträtfoto einer Frau mit gepflegter Haut, die eine weiße Frangipaniblüte an die Wange hält"></div>

  <header class="abs brand">
    <div class="brand-kind">KOSMETIKINSTITUT</div>
    <div class="brand-name">VELOURNA</div>
    <div class="brand-tagline">… EINFACH SCHÖN!</div>
  </header>

  <div class="abs col-taupe"></div>
  <div class="abs col-slate"></div>
  <div class="abs services-panel"></div>
  <h2 class="abs services-title" style="margin:0;font-weight:300;">UNSERE LEISTUNGEN:</h2>

  <div class="abs svc-head ruled" style="top:526px;">MASSAGEN</div>
  <div class="abs svc-item" style="top:554px;">klassische Massagen</div>
  <div class="abs svc-item" style="top:578px;">manuelle Lymphdrainage</div>

  <div class="abs svc-head ruled" style="top:623px;">RÜCKENBEHANDLUNG</div>
  <div class="abs svc-head ruled" style="top:648px;">SUGARING/WAX</div>
  <div class="abs svc-head ruled" style="top:672px;">GESICHTSBEHANDLUNG</div>
  <div class="abs svc-item" style="top:699px;">Microneedling</div>

  <div class="abs svc-head ruled" style="top:744px;">AUGENBLICKE</div>
  <div class="abs svc-item" style="top:771px;">Wimpern, Augenbrauen färben</div>
  <div class="abs svc-item" style="top:795px;">Augenbrauen zupfen</div>

  <div class="abs svc-head ruled" style="top:841px;">MAKE UP</div>
  <div class="abs svc-item" style="top:868px;">Permanent Make up</div>
  <div class="abs svc-item" style="top:892px;">Braut Make up</div>
  <div class="abs svc-item" style="top:917px;">Tages- und Abend Make up</div>

  <div class="abs svc-head ruled" style="top:962px;">WIRKSTOFFAMPULLEN</div>

  <div class="abs svc-head ruled" style="top:1011px;">HAND, FUSS- UND<br>NAGELPFLEGE</div>
  <div class="abs svc-item" style="top:1062px;">Refill</div>
  <div class="abs svc-item" style="top:1086px;">Maniküre</div>
  <div class="abs svc-item" style="top:1110px;">Zehenmodellage</div>
  <div class="abs svc-item" style="top:1141px;">Pediküre</div>

  <div class="abs slogan">. . . EINFACH SCHÖN!</div>

  <div class="abs photo-facial" role="img" aria-label="Foto einer Gesichtsbehandlung: eine rosa Maske wird mit einem Pinsel aufgetragen"></div>
  <div class="abs photo-brushes" role="img" aria-label="Foto von Make-up-Pinseln in einem Glas neben Puderpaletten und Lippenstift"></div>

  <div class="abs info-box"></div>
  <div class="abs info-text">WEITERE INFOS UND TERMIN-<br>VEREINBARNG UNTER:</div>

  <address class="abs contact" style="font-style:normal;">
    <p>Kosmetikinstitut Velourna</p>
    <p>Kettla Wundo</p>
    <p>Lindenweg 12</p>
    <p>79999 Musterau</p>
    <p>Tel. +49 70 00-12 34 56</p>
    <p>www.velourna-musterau.de</p>
  </address>
</main>
</body>
</html>
```